Premium Lawn fertiliser packaging - Looking for long term designer

*Update at bottom
I need a carefully considered, bold and professional packaging design for my new premium lawn fertiliser product. This contest is for a detailed front of the stand-up pouch packaging and once I’ve chosen a winner, they’ll be asked to create the layout for the back that links to the front as well. I have a full range of additional products that will also need designs and so I'm looking for someone who can do a great job here and who we can work with long term.

The front should include our logo for Pemberly Turf Supply Direct and be titled “Bloom Vigor Max” "Professional Lawn Fertiliser". The spring fertiliser tag line is "Awaken your lawn: Lush Greening, Lasting Health".
Beneath it, it then needs to include some important usage information and the key benefits along with some suitable graphic.

Key information to include:

Apply March - June
Treats 35-50 m2
16-3-8
+2%MgO + 1% Fe + 2.9% CaO (this is the chemical makeup of the fertiliser and needs to be fairly prominent. If you look at other professional fertiliser packaging, you'll see how it needs to compare).

Key features:
Premium fertiliser, used by professionals
Advanced greening with micro-nutrient complex
Dual action Nitrogen: Instant green boost & continuous feed for 3 months
Child & pet safe

Our brand colours are purple and green. Purple = #592999, Green = 3cb64a / 81d742 / 4d9d44

I think these colours look great against a white background.

Please make sure you look at our website as well to get an idea of our brand: www.pemberlyturfsupply.co.uk

To help, I've attached images of competitors fertiliser packaging that I like the look of. I'm not looking for you to copy but just see what type of thing appeals to me, the standard I'm expecting and what I need to compete against....

In addition, I have also attached some potential images you may wish to try using in your design, although please feel free to use your own if you have something better. For the moment, the images are 'preview' images, but once I decide on a design and we agree on the correct image, I will download and send over a fully licensed version.

*** Update*** When submitting your design, can you submit it in 2 formats: The first as a fully printed custom stand-up pouch and the second as a full-size label stuck onto a standup pouch (whatever colour you think is right for your design - choose white if you are not sure). To explain, I've just discovered we won't be able to get full custom bags printed in time for the first run and so we will have to opt for the design to be printed on labels and fixed onto bags. I therefore need to choose a design that works in both formats as both a label on a standup pouch as well as a fully printed pouch. Many thanks.

Target Market(s)

Domestic home-owners

Industry/Entity Type

Lawn care. NOT AGRICULTURE OR FARMING

Font styles to use
Sans Serif

Requirements
Must have
• Presented in 2 formats - see update at bottom of description
Nice to have
• I quite like designs against a white background, although I’m open to other ideas as well.
Should not have
• Please do not include any people or faces in the design. The text should be solid in colour, so no graduated colour fill in the text or outline text. Please avoid over-busy or cluttered designs.

```html
<!DOCTYPE html>
<html lang="en">
<head>
<meta charset="UTF-8">
<title>Bloom Vigor Max – Professional Lawn Fertiliser</title>
<link href="https://fonts.googleapis.com/css2?family=Anton&family=Roboto+Condensed:ital,wght@0,400;0,500;0,700;1,400;1,500&display=swap" rel="stylesheet">
<style>
  :root{
    --purple:#592999;
    --purple-deep:#4a2384;
    --green:#3cb64a;
    --green-lime:#81d742;
    --green-dark:#4d9d44;
    --white:#ffffff;
    --paper:#f4f4f4;
    --bag:#f7f7f7;
    --seal:#ececec;
    --rule:#d2d2d2;
  }
  *{box-sizing:border-box;margin:0;padding:0}
  html,body{width:1200px;height:800px;overflow:hidden;background:var(--paper)}
  body{font-family:"Roboto Condensed",sans-serif;color:var(--white)}
  .canvas{position:relative;width:1200px;height:800px}

  .pouch{position:absolute;left:330px;top:40px;width:540px;height:720px;
    background:var(--bag);border-radius:4px;overflow:hidden;
    box-shadow:0 18px 40px rgba(0,0,0,.12)}
  .seal{position:absolute;left:0;top:0;width:100%;height:56px;background:var(--seal);
    border-bottom:2px dashed var(--rule)}

  .brand{position:absolute;top:90px;left:0;width:100%;text-align:center}
  .brand-row{display:inline-flex;align-items:center;gap:10px}
  .brand-dot{width:26px;height:26px;border-radius:50%;background:var(--green)}
  .brand-name{font-weight:700;font-size:24px;color:var(--green-dark);letter-spacing:.5px}

  .title{position:absolute;top:148px;left:0;width:100%;text-align:center;
    font-family:"Anton",sans-serif;font-size:64px;line-height:1;color:var(--purple);letter-spacing:1px}
  .tagline{position:absolute;top:232px;left:0;width:100%;text-align:center;
    font-weight:700;font-size:19px;color:var(--purple)}
  .type-band{position:absolute;top:262px;left:50%;transform:translateX(-50%);
    background:var(--purple);padding:4px 12px;font-weight:700;font-size:26px;
    letter-spacing:.5px;white-space:nowrap}

  .scene{position:absolute;left:0;top:325px;width:100%;height:395px;
    background:linear-gradient(180deg,#5d7f86 0%,#3f7a3a 14%,#4f8f3a 40%,#5f8a48 62%,#6a5d8c 82%,var(--purple-deep) 100%)}

  .features{position:absolute;left:22px;top:382px;width:300px;list-style:none}
  .feature{display:flex;align-items:center;gap:12px;height:62px}
  .feature-icon{flex:none;width:46px;height:46px;border-radius:50%;background:var(--white);
    border:2px solid #e3e3e3;display:flex;align-items:center;justify-content:center}
  .feature-text{font-size:16px;line-height:1.15;font-weight:500;text-shadow:0 1px 2px rgba(0,0,0,.35)}

  .specs{position:absolute;right:26px;top:378px;width:190px;text-align:right}
  .spec-label{display:inline-block;background:var(--white);color:var(--green-dark);
    font-family:"Anton",sans-serif;font-size:20px;padding:1px 8px;border:1px solid #ccc}
  .spec-value{font-size:17px;font-weight:500;margin:6px 4px 10px 0;line-height:1.35;
    text-shadow:0 1px 2px rgba(0,0,0,.35)}

  .footer{position:absolute;left:22px;right:26px;bottom:22px;display:flex;align-items:flex-end;justify-content:space-between;gap:12px}
  .footer-notes{font-size:8px;font-style:italic;line-height:1.35;white-space:nowrap}
  .killer{background:var(--white);color:var(--purple);font-family:"Anton",sans-serif;
    font-size:17px;padding:1px 6px;border:1px solid #ccc;white-space:nowrap}
  .net{display:flex;align-items:center;gap:3px}
  .net-label{font-size:7px;writing-mode:vertical-rl;transform:rotate(180deg);font-weight:700}
  .net-num{font-family:"Anton",sans-serif;font-size:30px;line-height:1}
  .net-unit{display:flex;flex-direction:column;line-height:1}
  .net-unit b{font-family:"Anton",sans-serif;font-size:14px;font-weight:400}
  .net-unit span{font-size:7px}
</style>
</head>
<body>
<main class="canvas">
  <section class="pouch">
    <div class="seal"></div>

    <header class="brand">
      <div class="brand-row">
        <span class="brand-dot"></span>
        <span class="brand-name">Pemberly Turf Supply Direct</span>
      </div>
    </header>

    <h1 class="title">BLOOM VIGOR MAX</h1>
    <p class="tagline">Awaken your lawn: Lush Greening, Lasting Health</p>
    <p class="type-band">PROFESSIONAL LAWN FERTILISER</p>

    <div class="scene" role="img" aria-label="Photograph of a large house with a manicured green lawn and leafy trees"></div>

    <ul class="features">
      <li class="feature">
        <span class="feature-icon">
          <svg width="26" height="26" viewBox="0 0 26 26" fill="none" stroke="#3cb64a" stroke-width="2"><path d="M13 2l9 3v7c0 6-4 10-9 12C8 22 4 18 4 12V5z"/><path d="M8.5 13l3 3 6-6"/></svg>
        </span>
        <span class="feature-text">Child &amp; pet safe</span>
      </li>
      <li class="feature">
        <span class="feature-icon">
          <svg width="26" height="26" viewBox="0 0 26 26" fill="none" stroke="#3cb64a" stroke-width="2"><circle cx="13" cy="13" r="10"/><circle cx="13" cy="13" r="5"/></svg>
        </span>
        <span class="feature-text">Premium fertiliser,<br>used by professionals</span>
      </li>
      <li class="feature">
        <span class="feature-icon">
          <svg width="26" height="26" viewBox="0 0 26 26" fill="none" stroke="#3cb64a" stroke-width="2"><path d="M13 24V11"/><path d="M13 13c0-4-3-6-7-6 0 4 3 6 7 6z"/><path d="M13 11c0-4 3-6 7-6 0 4-3 6-7 6z"/></svg>
        </span>
        <span class="feature-text">Advanced greening<br>with micro-nutrient complex</span>
      </li>
      <li class="feature">
        <span class="feature-icon">
          <svg width="26" height="26" viewBox="0 0 26 26" fill="none" stroke="#3cb64a" stroke-width="2"><path d="M13 3c4 6 7 9 7 13a7 7 0 0 1-14 0c0-4 3-7 7-13z"/></svg>
        </span>
        <span class="feature-text">Dual action Nitrogen:<br>Instant green boost &amp;<br>continuous feed for 3 months</span>
      </li>
    </ul>

    <aside class="specs">
      <span class="spec-label">APPLY</span>
      <p class="spec-value">March - June</p>
      <span class="spec-label">TREATS</span>
      <p class="spec-value">35-50 m2</p>
      <span class="spec-label">RATIO</span>
      <p class="spec-value">16-3-8 + 2% MgO<br>+1% Fe + 2.9% CaO</p>
    </aside>

    <footer class="footer">
      <p class="footer-notes">Everything your lawn needs for the season<br>Requires up to 30% less water year after year<br>Covers up to five thousand square feet</p>
      <span class="killer">WEED AND MOSS KILLER</span>
      <div class="net">
        <span class="net-label">NET WT.</span>
        <span class="net-num">10</span>
        <span class="net-unit"><b>LBS</b><span>4.54 KG</span></span>
      </div>
    </footer>
  </section>
</main>
</body>
</html>
```